Veltrisk inc. Aviation website

we are looking for a very modern and luxury web design, we are an aviation based company and specialize in aircraft exports and setup of air services world wide.
we want the website to be unique, creative, luxurious, professional, and to make an statement.
we have attached the logo.
our business cards theme is black background with gold stamping, if that is the rout you want to take.
**The format we are looking for is Wordpress.**
**the website is www.veltriskinc-example.com**
** 3 pages:
1. home page: -overview/about us
-industry leading
- worldwide presence
- aerial support
2. products and services: -business aircrafts
-commercial aircrafts
-amphibious aircrafts
-operation setup
-maintenance & crew training
3. contact us
**our location: Marlow Fenwick Harbour Airfield, Hangar 6**
we do appreciate suggestions
Thank you all.
Target Market(s)
Aviation professionals, Aircraft import/export, airlines, air taxi operations
Industry/Entity Type
It Company
Number of Pages Required
3 page
Requirements
Must have
- must have a very modern and luxurious design, and must be aviation oriented, and must have the logo, must be professional looking and be animated.
Nice to have
- black, gold, and burgandy colour
Should not have
- should not be playful and cartoony.

```html
<!DOCTYPE html>
<html lang="en">
<head>
<meta charset="utf-8">
<title>Veltrisk inc. — Aviation</title>
<link href="https://fonts.googleapis.com/css2?family=Roboto:wght@300;400;500;700&family=Oswald:wght@400;500&display=swap" rel="stylesheet">
<style>
:root{
  --burgundy:#9b1c24;
  --accent:#b3232b;
  --gold:#d8b21e;
  --ink:#2a2a2a;
  --muted:#8a8a8a;
  --footer:#1f1f1f;
  --footer-bottom:#141414;
  --white:#ffffff;
}
*{margin:0;padding:0;box-sizing:border-box}
html,body{width:674px;height:1200px;overflow:hidden;background:var(--white)}
body{font-family:"Roboto",Arial,sans-serif;color:var(--ink);position:relative}
.abs{position:absolute}

.topbar{left:0;top:0;width:674px;height:20px;background:var(--burgundy);color:var(--white);font-size:7px}
.topbar .contact{left:54px;top:6px;display:flex;gap:14px;align-items:center}
.topbar .contact span{display:flex;align-items:center;gap:3px}
.topbar .tools{right:54px;top:5px;display:flex;gap:5px;align-items:center}
.topbar .sq{width:8px;height:8px;background:var(--white);border-radius:1px}
.topbar .divider{width:1px;height:20px;background:rgba(255,255,255,.3);margin:0 6px}

.header{left:0;top:20px;width:674px;height:54px;background:var(--white)}
.brand{left:50px;top:17px;display:flex;align-items:center;gap:6px}
.brand .mark{width:16px;height:16px;background:var(--gold);border-radius:50%}
.brand .name{font-size:18px;font-weight:400;letter-spacing:1.5px;color:var(--burgundy)}
.nav{right:52px;top:24px;display:flex;gap:24px;font-size:8.6px;color:#222}
.nav .active{color:var(--accent)}

.hero{left:0;top:74px;width:674px;height:297px;background:radial-gradient(ellipse at 50% 20%,#c9a24c 0%,#8a6a2c 35%,#3a3022 70%,#1e1a16 100%)}
.hero .title{width:100%;text-align:center;top:116px;font-family:"Oswald",sans-serif;color:var(--white);font-size:38px;font-weight:500;letter-spacing:.5px;text-shadow:0 2px 4px rgba(0,0,0,.4)}
.hero .sub{width:100%;text-align:center;top:164px;font-family:"Oswald",sans-serif;color:var(--white);font-size:22px;text-shadow:0 2px 4px rgba(0,0,0,.4)}
.hero .arrow{top:152px;width:20px;height:20px;border-radius:50%;background:rgba(20,20,20,.8)}
.hero .arrow.prev{left:28px}.hero .arrow.next{left:628px}

.welcome h1{width:100%;top:400px;text-align:center;font-size:15.5px;font-weight:400;color:var(--ink)}
.welcome h1 em{font-style:normal;color:var(--accent)}
.welcome p{left:62px;width:550px;top:425px;text-align:center;font-size:7.6px;line-height:13.4px;color:#666;font-weight:300}

.feature{width:170px;text-align:center}
.feature .photo{width:102px;height:102px;border-radius:50%;margin:0 auto;border:3px solid #eee}
.feature h3{margin-top:12px;font-size:8px;font-weight:400;color:#222}
.feature p{margin:6px auto 0;width:130px;font-size:7px;line-height:11px;color:var(--muted);font-weight:300}
.feature a{display:block;margin-top:8px;font-size:6.6px;color:var(--accent);text-decoration:none}
.f1{left:51px;top:492px}.f2{left:250px;top:492px}.f3{left:447px;top:492px}
.f1 .photo{background:radial-gradient(circle,#d89a4a,#3c5a78 60%,#1c2a3a)}
.f2 .photo{background:radial-gradient(circle at 40% 40%,#6ec0ee,#1a5aa6 55%,#0a2a5c)}
.f3 .photo{background:linear-gradient(160deg,#f2c06c,#b06a4a 55%,#4a3440)}

.opportunity{left:0;top:698px;width:335px;height:175px;background:var(--gold);color:var(--white)}
.opportunity h2{position:absolute;left:50px;top:38px;font-size:14.5px;font-weight:500}
.opportunity p{position:absolute;left:50px;top:62px;width:260px;font-size:7px;line-height:11.2px}
.opp-photo{left:335px;top:698px;width:339px;height:175px;background:linear-gradient(170deg,#1c4ea0 0%,#4a7cc4 45%,#a9c4e6 70%,#5c86c2 100%)}

.blog h2{left:53px;top:908px;font-size:12.5px;font-weight:400;color:#222}
.blog h2 em{font-style:normal;color:var(--accent)}
.blog .pager{left:610px;top:910px}
.post{width:290px;height:80px}
.post .thumb{position:absolute;left:0;top:0;width:91px;height:80px}
.post .body{position:absolute;left:100px;top:6px;width:190px}
.post h4{font-size:8px;font-weight:400;color:#333}
.post .date{font-size:6.6px;margin-top:5px;color:#333}
.post p{font-size:5.8px;line-height:10.5px;color:#555;margin-top:3px}
.post a{display:block;font-size:6.6px;color:var(--accent);margin-top:4px;text-decoration:none}
.p1{left:53px;top:942px}.p2{left:356px;top:942px}
.p1 .thumb{background:linear-gradient(160deg,#c8b49a,#8a7460 60%,#4a4038)}
.p2 .thumb{background:linear-gradient(180deg,#d8dce4,#5a6a8a 40%,#c8ccd4)}
.p2 .body{top:2px}

.footer{left:0;top:1050px;width:674px;height:118px;background:var(--footer);color:var(--white)}
.footer .brand-f{position:absolute;left:52px;top:50px;font-size:16px;letter-spacing:1.5px;display:flex;align-items:center;gap:6px}
.footer .brand-f .mark{width:14px;height:14px;border-radius:50%;background:var(--white)}
.footer h5{font-size:8.6px;font-weight:400;letter-spacing:.3px}
.footer .col{position:absolute;top:22px}
.c-contact{left:221px}.c-news{left:360px}.c-social{left:542px}
.c-contact .addr{font-size:7px;line-height:11px;margin-top:8px}
.c-contact .row{display:flex;align-items:center;gap:6px;margin-top:6px;font-size:9px}
.c-contact .row.small{font-size:7px;margin-top:4px}
.c-news p{font-size:6.4px;line-height:11px;margin-top:8px;width:150px}
.c-news form{display:flex;margin-top:10px}
.c-news .input{width:94px;height:21px;background:var(--white);color:#888;font-size:5.8px;padding:7px 7px;border:1px solid var(--gold)}
.c-news .btn{width:47px;height:21px;background:var(--gold);color:var(--white);font-size:8.4px;display:flex;align-items:center;justify-content:center}
.c-social .icons{display:flex;gap:10px;margin-top:11px}
.c-social .icons span{width:19px;height:19px;background:var(--white);border-radius:2px}
.copyright{left:0;top:1168px;width:674px;height:32px;background:var(--footer-bottom);color:var(--white);font-size:7.4px;text-align:center;line-height:32px}
</style>
</head>
<body>

<div class="abs topbar">
  <div class="abs contact">
    <span><svg width="7" height="7" viewBox="0 0 10 10"><path d="M2 1l2 2-1 1.5c.6 1.2 1.4 2 2.5 2.5L7 6l2 2-1.5 1.5C4 9 1 6 .5 2.5z" fill="#fff"/></svg>: 0490 118 372</span>
    <span><svg width="8" height="6" viewBox="0 0 10 7"><rect x=".5" y=".5" width="9" height="6" fill="none" stroke="#fff"/><path d="M.5 .5l4.5 3.5 4.5-3.5" fill="none" stroke="#fff"/></svg>:hello@veltriskinc-example.com</span>
  </div>
  <div class="abs tools">
    <svg width="8" height="8" viewBox="0 0 10 10"><circle cx="4" cy="4" r="3" fill="none" stroke="#fff" stroke-width="1.4"/><path d="M6.2 6.2L9 9" stroke="#fff" stroke-width="1.4"/></svg>
    <span class="divider"></span>
    <span class="sq"></span><span class="sq"></span><span class="sq"></span><span class="sq"></span>
  </div>
</div>

<header class="abs header">
  <div class="abs brand"><span class="mark"></span><span class="name">VELTRISK</span></div>
  <nav class="abs nav">
    <span class="active">HOME</span><span>ABOUT US</span><span>SERVICES</span><span>MEMBERS</span><span>BLOG</span><span>CONTACTS</span>
  </nav>
</header>

<section class="abs hero" role="img" aria-label="Airliner taking off over a lit runway at sunset">
  <div class="abs title">VELTRISK</div>
  <div class="abs sub">AERIAL SUPPORT</div>
  <div class="abs arrow prev"><svg width="20" height="20" viewBox="0 0 20 20"><path d="M11.5 6l-4 4 4 4" fill="none" stroke="#fff" stroke-width="1.6"/></svg></div>
  <div class="abs arrow next"><svg width="20" height="20" viewBox="0 0 20 20"><path d="M8.5 6l4 4-4 4" fill="none" stroke="#fff" stroke-width="1.6"/></svg></div>
</section>

<section class="welcome">
  <h1 class="abs">WELCOME TO <em>VELTRISK INC.</em></h1>
  <p class="abs">Lorem Ipsum has been the industry's standard dummy text ever since the 1500s, when an unknown printer took a galley of type and scrambled it to make a type specimen book. It has survived not only five centuries, but also the leap into electronic typesetting, remaining essentially unchanged. It was popularised in the 1960s with the release of Quillmark sheets containing Lorem Ipsum passages, and more recently with desktop publishing software</p>
</section>

<div class="abs feature f1">
  <div class="photo" role="img" aria-label="Industrial pipework lit at dusk"></div>
  <h3>INDUSTRY LEADING</h3>
  <p>Lorem Ipsum has been the industry's standard dummy text ever since</p>
  <a href="#">Read More -&gt;</a>
</div>
<div class="abs feature f2">
  <div class="photo" role="img" aria-label="Blue digital globe"></div>
  <h3>WORLDWIDE PRESENCE</h3>
  <p>Lorem Ipsum has been the industry's standard dummy text ever since</p>
  <a href="#">Read More -&gt;</a>
</div>
<div class="abs feature f3">
  <div class="photo" role="img" aria-label="Passenger jet flying in a golden sky"></div>
  <h3>AERIAL SUPPORT</h3>
  <p>Lorem Ipsum has been the industry's standard dummy text ever since</p>
  <a href="#">Read More -&gt;</a>
</div>

<section class="abs opportunity">
  <h2>GLOBAL OPPORTUNITY</h2>
  <p>Lorem Ipsum has been the industry's standard dummy text ever since the 1500s, when an unknown printer took a galley of type and scrambled it to make a type specimen book. It has survived not only five centuries, but also the leap into electronic typesetting, remaining essentially unchanged. It was popularised in the 1960s with the release of Quillmark sheets containing Lorem Ipsum passages, and more recently with desktop publishing software like Brevant PageSetter including versions of Lorem Ipsum</p>
</section>
<div class="abs opp-photo" role="img" aria-label="Wide-body jet climbing through a blue sky"></div>

<section class="blog">
  <h2 class="abs">LATEST <em>BLOG</em></h2>
  <svg class="abs pager" width="14" height="10" viewBox="0 0 14 10"><path d="M5 1L1 5l4 4M9 1l4 4-4 4" fill="none" stroke="#222" stroke-width="1.3"/></svg>
  <article class="abs post p1">
    <div class="thumb" role="img" aria-label="Military helicopter in flight"></div>
    <div class="body">
      <h4>Nemo Enim Ipsam Volup</h4>
      <div class="date">09-07-2016</div>
      <p>Lorem Ipsum has been the industry's standard dummy text ever since the 1500s, when an unknown printer took a galley of type and scrambled it to make a type specimen book.</p>
      <a href="#">Read More &gt;&gt;</a>
    </div>
  </article>
  <article class="abs post p2">
    <div class="thumb" role="img" aria-label="Empty airport terminal corridor"></div>
    <div class="body">
      <h4>Nemo Enim Ipsam Volup</h4>
      <div class="date">09-07-2016</div>
      <p>Lorem Ipsum has been the industry's standard dummy text ever since the 1500s, when an unknown printer took a galley of type and scrambled it to make a type specimen book.</p>
      <a href="#">Read More &gt;&gt;</a>
    </div>
  </article>
</section>

<footer class="abs footer">
  <div class="brand-f"><span class="mark"></span><span>VELTRISK</span></div>
  <div class="col c-contact">
    <h5>CONTACT US</h5>
    <div class="addr">Hangar 6, Marlow Fenwick<br>Harbour Airfield</div>
    <div class="row"><svg width="10" height="10" viewBox="0 0 10 10"><path d="M2 1l2 2-1 1.5c.6 1.2 1.4 2 2.5 2.5L7 6l2 2-1.5 1.5C4 9 1 6 .5 2.5z" fill="none" stroke="#fff" stroke-width=".8"/></svg>555-214-0968</div>
    <div class="row small"><svg width="11" height="8" viewBox="0 0 11 8"><rect x=".5" y=".5" width="10" height="7" fill="none" stroke="#fff" stroke-width=".8"/><path d="M.5 .5l5 4 5-4" fill="none" stroke="#fff" stroke-width=".8"/></svg>hello@veltriskinc-example.com</div>
  </div>
  <div class="col c-news">
    <h5>NEWSLETTER</h5>
    <p>Excepteur sint occaecat cupidatat non proident, sunt in culpa qui officia deserunt mollit anim</p>
    <form><div class="input">Enter your email address</div><div class="btn">Sign Up</div></form>
  </div>
  <div class="col c-social">
    <h5>SOCIAL MEDIA</h5>
    <div class="icons"><span></span><span></span><span></span></div>
  </div>
</footer>
<div class="abs copyright">2016 &nbsp;All Rights Reserved.</div>

</body>
</html>
```